Business Cards for our company

Hi there,

we have successfully designed a logo with ArtFlock and would like now to design our business cards. We would like to keep the colours and the look-and-feel of the logo. Please send in variations with two or three colours and one or two sides. I promise to respond to every single submission.

Many thanks and happy new year.

All the best,
Wilfried

Target Market(s)

B2B

Industry/Entity Type

Trade

Contact Information for Business Card

We have successfully designed a logo with ArtFlock and would like now to design our business cards. We would like to keep the colours and the look-and-feel of the logo. Please send in variations with two or three colours and one or two sides. I promise to respond to every single submission.

Font styles to use
Serif
Sans Serif
Script

Requirements
Must have
• These information should be on the business card, grouped as you suggest, and we think using small pictograms for mobile, email, etc is pretty helpful:
• Wilfried Tammler (first and second name)
• Geschäftsführer/ Managing Director (title)
• KoR Warenkontor GmbH (company name and legal form)
• Ostheimer Str. 18/3 (street and house number)
• 70999 Talbrunn (zip code and town)
• +491709384562 (mobile)
• +4971569027341 (work)
• w.tammler@kor-warenkontor.example (email)
• www.kor-warenkontor.example (web)
Nice to have
• Spectacular and interesting layout and design. You look at it and think, wow, that's not the normal stuff.
• We think of ourselves as bridge-builders between businesses (international producers on the one hand, and retail chains on the other hand) and we translate, organise and manage projects where both partners are involved, but it's difficult for them to cooperate due to language barriers and different working cultures.
• This is why we have the n between the B's shaped as a bridge, and the green arc supports this idea. Maybe you could play with this idea...
Should not have
• the standard layout that everybody has

```html
<!DOCTYPE html>
<html lang="de">
<head>
<meta charset="utf-8">
<title>KoR Warenkontor – Visitenkarte</title>
<link href="https://fonts.googleapis.com/css2?family=Roboto:wght@400;700&display=swap" rel="stylesheet">
<style>
  :root {
    --green: #2eac4b;
    --black: #07080a;
    --white: #ffffff;
    --ink: #1c1c1c;
    --backdrop: #6a4744;
  }
  html, body {
    margin: 0;
    width: 1200px;
    height: 1200px;
    overflow: hidden;
    background: var(--backdrop);
    font-family: "Roboto", Arial, sans-serif;
  }
  .card {
    position: absolute;
    left: 276px;
    width: 647px;
    height: 410px;
    overflow: hidden;
    box-shadow: 0 6px 14px rgba(0,0,0,.45);
  }
  .card--front { top: 160px; background: var(--white); }
  .card--back { top: 628px; background: var(--black); }

  .brand-name {
    position: absolute;
    margin: 0;
    font-weight: 700;
    font-size: 40px;
    line-height: 1.1;
    text-align: center;
  }
  .card--front .brand-name {
    left: 10px; width: 270px; top: 128px;
    color: var(--black);
  }
  .card--back .brand-name {
    left: 0; width: 100%; top: 160px;
    color: var(--white);
  }

  .divider {
    position: absolute;
    left: 289px; top: 44px;
    width: 2px; height: 292px;
    background: var(--green);
  }
  .contact-block {
    position: absolute;
    left: 311px; top: 50px;
    color: var(--ink);
  }
  .person-name {
    margin: 0;
    font-size: 26px;
    font-weight: 700;
    color: var(--green);
    line-height: 32px;
  }
  .person-title {
    margin: 0 0 10px;
    font-size: 17.5px;
    line-height: 24px;
  }
  .contact-list {
    list-style: none;
    margin: 0 0 12px;
    padding: 0;
  }
  .contact-list li {
    display: flex;
    align-items: center;
    font-size: 17px;
    line-height: 23px;
    white-space: nowrap;
  }
  .contact-list svg {
    width: 14px; height: 14px;
    margin-right: 10px;
    flex: none;
    fill: var(--green);
  }
  .company-address {
    font-style: normal;
    font-size: 18px;
    line-height: 23px;
  }
  .company-address strong { font-weight: 700; }

  .footer-bands {
    position: absolute;
    left: 0; bottom: 0;
    width: 647px; height: 60px;
  }
</style>
</head>
<body>

<section class="card card--front">
  <p class="brand-name">KoR<br>Warenkontor</p>

  <div class="divider"></div>

  <div class="contact-block">
    <h1 class="person-name">Wilfried Tammler</h1>
    <p class="person-title">Geschäftsführer / Managing Director</p>

    <ul class="contact-list">
      <li>
        <svg viewBox="0 0 14 14" aria-hidden="true"><path d="M4 1h6a1 1 0 0 1 1 1v10a1 1 0 0 1-1 1H4a1 1 0 0 1-1-1V2a1 1 0 0 1 1-1zm.6 1.6v7.6h4.8V2.6z"/></svg>
        +49 170 9384562
      </li>
      <li>
        <svg viewBox="0 0 14 14" aria-hidden="true"><path d="M1 5c2-3 10-3 12 0l-1 2-2.5-1V4.5c-1.5-.5-3.5-.5-5 0V6L2 7zM3 8h8l1 4H2z"/></svg>
        +49 7000 9027341
      </li>
      <li>
        <svg viewBox="0 0 14 14" aria-hidden="true"><path d="M4 1h6v3H4zM1 5h12v6h-2V9H3v2H1zM4 10h6v3H4z"/></svg>
        +49 7000 9027342
      </li>
      <li>
        <svg viewBox="0 0 14 14" aria-hidden="true"><path d="M1 3h12v8H1zm1.2 1.2L7 7.6l4.8-3.4v-.2H2.2zm0 1.5v4.1h9.6V5.7L7 9z"/></svg>
        w.tammler@kor-warenkontor.example
      </li>
      <li>
        <svg viewBox="0 0 14 14" aria-hidden="true"><path d="M7 1a6 6 0 1 0 0 12A6 6 0 0 0 7 1zm0 1.2c.8.8 1.3 2.2 1.5 4.2h-3C5.7 4.4 6.2 3 7 2.2zM2.3 6.4c.2-2 1.5-3.5 3.2-4-.6 1-1 2.4-1.1 4zm5.9 5.4c.6-1 1-2.4 1.1-4h2.4c-.2 2-1.7 3.5-3.5 4zM5.5 7.6h3c-.2 2-.7 3.4-1.5 4.2-.8-.8-1.3-2.2-1.5-4.2zm-3.2 0h2.1c.1 1.6.5 3 1.1 4-1.7-.5-3-2-3.2-4zm7.3-1.2c-.1-1.6-.5-3-1.1-4 1.8.5 3.2 2 3.5 4z"/></svg>
        www.kor-warenkontor.example
      </li>
    </ul>

    <address class="company-address">
      <strong>KoR Warenkontor GmbH</strong><br>
      Ostheimer Str. 18/3<br>
      70999 Talbrunn<br>
      Deutschland
    </address>
  </div>

  <svg class="footer-bands" viewBox="0 0 647 60" aria-hidden="true">
    <polygon points="0,20 300,20 340,60 0,60" fill="var(--green)"/>
    <polygon points="328,46 647,46 647,60 342,60" fill="var(--black)"/>
  </svg>
</section>

<section class="card card--back">
  <p class="brand-name">KoR<br>Warenkontor</p>
</section>

</body>
</html>
```